Brimvale Crest Homes needs a business card

We need a business card for a new company in Canada, Ontario. Our company is all about luxury contraction homes for our clients. Our product and services are custom projects design. Under the business logo that will be created, we want a slogan that will be a memorable phrase for consumers to remember us to tell their friends and relatives.

Additional infomation
- Teodoro Vanlesky
- President / Ceo
-519.304.7718

Find point what luxury construction products and services can be done

We like to see colors:
- #663300
- and something other colors or color that would attract the client needs and wants

The final design should communicate leads from new or old clients that will grow our empire. Most of all, we try to work among the budget that clients want

NOTE
- we also need an icon for the business (Example: Instagram, Facebook, and Whatsapp icons)
- We want the company name to be remembered easily for clients and our distributors who would get our orders.
- we need an icon on the business cards: Facebook and Instagram.

Thanks,
Brimvale Crest Homes

```html
<!DOCTYPE html>
<html lang="en">
<head>
<meta charset="utf-8">
<title>Brimvale Crest Homes — Business Card</title>
<link rel="stylesheet" href="https://fonts.googleapis.com/css2?family=Ubuntu:wght@400;700&family=Open+Sans:wght@400&family=Noto+Sans:wght@400&display=swap">
<style>
  :root {
    --brown: #663300;
    --ink: #000000;
    --paper: #ffffff;
  }
  html, body {
    margin: 0;
    padding: 0;
    width: 1200px;
    height: 1200px;
    overflow: hidden;
    background: var(--paper);
  }
  .canvas {
    position: relative;
    width: 1200px;
    height: 1200px;
  }
  .card-shapes {
    position: absolute;
    inset: 0;
  }
  .txt {
    position: absolute;
    margin: 0;
    white-space: nowrap;
    line-height: 1;
  }
  .front-wordmark {
    left: 101px;
    width: 348px;
    top: 392px;
    text-align: center;
    font-family: "Ubuntu", sans-serif;
    font-weight: 700;
    font-size: 44px;
    line-height: 1.08;
    color: var(--ink);
    white-space: normal;
  }
  .front-name {
    left: 101px;
    width: 348px;
    top: 744px;
    text-align: center;
    font-family: "Ubuntu", sans-serif;
    font-weight: 700;
    font-size: 27px;
    color: var(--brown);
  }
  .front-tagline {
    left: 101px;
    width: 348px;
    top: 777px;
    text-align: center;
    font-family: "Open Sans", sans-serif;
    font-size: 9.5px;
    color: var(--brown);
  }
  .front-band-text {
    left: 101px;
    width: 348px;
    top: 905px;
    text-align: center;
    font-family: "Open Sans", sans-serif;
    font-size: 8px;
    color: var(--paper);
  }
  .back-mark {
    position: absolute;
    left: 517px;
    top: 642px;
    width: 40px;
    height: 39px;
    background: var(--brown);
  }
  .back-name {
    left: 564px;
    top: 641px;
    font-family: "Ubuntu", sans-serif;
    font-weight: 700;
    font-size: 26px;
    color: var(--paper);
  }
  .back-tagline {
    left: 571px;
    top: 669px;
    font-family: "Open Sans", sans-serif;
    font-size: 9.5px;
    color: var(--paper);
  }
  .person-name {
    left: 565px;
    top: 745px;
    font-family: "Ubuntu", sans-serif;
    font-weight: 700;
    font-size: 16.5px;
    color: var(--paper);
  }
  .person-role {
    left: 565px;
    width: 168px;
    top: 765px;
    text-align: center;
    font-family: "Ubuntu", sans-serif;
    font-size: 16.5px;
    color: var(--paper);
  }
  .contact {
    position: absolute;
    left: 775px;
    top: 787px;
    margin: 0;
    font-family: "Noto Sans", sans-serif;
    font-size: 17px;
    line-height: 20.4px;
    color: var(--paper);
    font-style: normal;
  }
</style>
</head>
<body>
<main class="canvas">
  <svg class="card-shapes" width="1200" height="1200" viewBox="0 0 1200 1200" aria-hidden="true">
    <!-- front card -->
    <rect class="front-top" x="101.25" y="291.25" width="348.15" height="340.65" fill="var(--brown)"/>
    <rect class="front-body" x="101.25" y="631.9" width="348.15" height="271.85" fill="var(--ink)"/>
    <rect class="front-band" x="101.25" y="903.75" width="348.15" height="12.5" fill="var(--brown)"/>
    <!-- back card -->
    <polygon class="back-body"
      points="653.75,568.75 1106.25,568.75 1106.25,916.25 481.25,916.25 481.25,741.25 518.1,704.4 496.25,704.4 496.25,622.5 601.25,622.5"
      fill="var(--ink)"/>
  </svg>

  <section class="card card-front">
    <p class="txt front-wordmark">Brimvale<br>Crest<br>Homes</p>
    <h1 class="txt front-name">Brimvale Crest Homes</h1>
    <p class="txt front-tagline">- HOME RENOVATIONS - CUSTOM PROJECT DESIGN -</p>
    <p class="txt front-band-text">GOOD HOME RENOVATION, BRIMVALE CREST HOMES</p>
  </section>

  <section class="card card-back">
    <div class="back-mark"></div>
    <h2 class="txt back-name">Brimvale Crest Homes</h2>
    <p class="txt back-tagline">- HOME RENOVATIONS - CUSTOM PROJECT DESIGN -</p>
    <p class="txt person-name">Teodoro Vanlesky</p>
    <p class="txt person-role">CEO</p>
    <address class="contact">
      12345 Street Name , ste.101<br>
      City Place ,VA 28746<br>
      Ph. 519.304.7718<br>
      Fax 519.304.7718
    </address>
  </section>
</main>
</body>
</html>
```